Professional and modern website for Real Estate services company

Hi there! We're looking for a responsive, highly professional and modern (in line with Latest trends) coded website for a Real Estate services company named Portalia720º (find logo attached). I will try to Explain how I picture it in my head, but feel free to step out of the script and design it as you please. The structure for the website must be as Follows: - Menu: at the top of the screen, always visible (in any page and when to scrolling down). Logo at the left hand side (clicking redirects to home), then a Services, About us, Blog and Contact and on the right hand, Estimate and Log in (just placeholder, no log in required yet). - Home: (I like https://fr.domvera.example/): a landscape picture of Madrid's skyline. Very important That at a first glance (without scrolling) you can see a box to input data of your building to get an estimate (Post code, Number of homes, Number of garages, Number of stores, Swimming pool (yes / no) Concierge (yes / no)). Should there be a small space Also for a corporate presentation video (more or less like https://www.velbrastahogares.example/ but With the estimate Request box INSTEAD OF the App - however, do not take this one as example Given I just wanted to illustrate the structure). Still in the Home, bellow the first glance, I'd like to have a brief introduction of the following pages (Services, About us, Blog and Contact). This can be in a Either "square" form (like https://fr.domvera.example/) or in a "scroll" form (like https://k7pisos.example/). - Services: we offer 3 sets of services, each of them composed by three specific services, Namely: * Administration Treasury Accounting Savings * Consulting Legal Technical Regulatory * Mediation Repairs Meetings Delinquency For the sake of structuring, each of the nine services will Have to written description composed of 3 small paragraphs of About 15 words. I Tend to like to Accompany With each of the services related icons / vectors, but feel free to design them as you want. - About us: content not yet defined, but will be a series of bullets / sections in Which We talk about prep or differentiating points. We can include the corporate video presentation here again. - Blog: just a space Where you can see to the blog entries (in Home, probably just show 3/4). - Contact: a fancy contact form, with map, address, telephone, e-mail and opening hours. Just to give it a bit more content, maybe include a catch phrase like "We're looking forward to meeting you!" or something like that. - Estimate: this is the Most Important page in the website (in Addition to the upper part of the Home page). Basically replicate the estimate for the home box, but maybe with a bit more design or extended, Given this is a single page just for that. - Log in: opens a drop-down with user and password (just placeholder, no log in required yet). Regarding colors, we still do not Have a color scheme, so anything in line With the logo is OK. Many thanks in advance, Martin

All ages and genders

Real Estate

Coded - Design and coding required

5+ page

Sans Serif

Must have
• Blank colored background

```html
<!DOCTYPE html>
<html lang="en">
<head>
<meta charset="utf-8">
<title>Portalia720º — Real Estate Services</title>
<link href="https://fonts.googleapis.com/css2?family=Roboto:wght@400;500;700;900&family=Roboto+Condensed:wght@700&display=swap" rel="stylesheet">
<style>
:root{
  --orange:#d9700f;
  --orange-deep:#c45f08;
  --orange-band:rgba(206,104,14,.88);
  --white:#ffffff;
  --ink:#3c3c3c;
  --muted:#6c6c6c;
  --light:#f3f1ef;
  --dark:#4a4a4a;
}
*{box-sizing:border-box;margin:0;padding:0}
html,body{width:1200px;height:3046px;overflow:hidden}
body{font-family:'Roboto',Arial,sans-serif;color:var(--ink);background:var(--white);position:relative}
section,header,footer{position:absolute;left:0;width:1200px}
.center{text-align:center}

/* top bar */
.topbar{top:0;height:20px;background:var(--orange);color:var(--white);font-size:9px;display:flex;align-items:center}
.topbar .contact{position:absolute;left:258px;display:flex;gap:26px}
.topbar .links{position:absolute;left:795px;display:flex;gap:14px;font-weight:500}

/* nav */
.nav{top:20px;height:78px;background:var(--white);border-bottom:1px solid #eee}
.brand{position:absolute;left:252px;top:24px;display:flex;align-items:center;gap:8px}
.brand-mark{width:16px;height:16px;background:var(--orange)}
.brand-name{font-size:30px;font-weight:700;color:var(--dark);letter-spacing:-.5px}
.menu{position:absolute;left:508px;top:36px;display:flex;gap:24px;font-size:11px;color:var(--muted)}
.menu .active{color:var(--orange);border-bottom:2px solid var(--orange);padding-bottom:4px}
.login{position:absolute;left:862px;top:30px;width:88px;height:24px;background:var(--orange);color:var(--white);font-size:10px;font-weight:700;display:flex;align-items:center;justify-content:center}

/* hero */
.hero{top:98px;height:434px}
.hero-photo{position:absolute;inset:0;background:linear-gradient(180deg,#9aa3ad 0%,#6c6a68 40%,#5a4535 65%,#d9dcdf 100%)}
.hero-band{position:absolute;left:0;top:146px;width:1200px;height:70px;background:var(--orange-band)}
.hero h1{position:absolute;top:152px;width:100%;text-align:center;color:var(--white);font-family:'Roboto Condensed',sans-serif;font-size:48px;font-weight:700}
.hero p{position:absolute;top:222px;left:300px;width:600px;text-align:center;color:var(--white);font-size:16px;line-height:22px}
.btn-ghost{position:absolute;left:566px;top:282px;width:68px;height:22px;border:1px solid var(--white);color:var(--white);font-size:9px;display:flex;align-items:center;justify-content:center}
.search{position:absolute;left:254px;top:420px;width:696px;height:34px;background:var(--orange);padding:4px;display:flex}
.search-input{flex:1;background:var(--white);font-size:10px;color:#888;padding:6px 8px}
.search-btn{width:52px;margin:-4px -4px -4px 4px;background:#4a4a4a;display:flex;align-items:center;justify-content:center}

/* headings */
.sec-title{font-family:'Roboto Condensed',sans-serif;font-size:36px;font-weight:700;text-align:center}
.divider{position:relative;width:140px;height:14px;margin:8px auto 0}
.divider::before{content:"";position:absolute;left:0;right:0;top:6px;height:1px;background:currentColor;opacity:.6}
.divider::after{content:"";position:absolute;left:64px;top:2px;width:10px;height:10px;background:currentColor;transform:rotate(45deg)}

/* about */
.about{top:532px;height:432px;background:linear-gradient(180deg,#f6f5f4 0%,#ecebea 100%)}
.about .sec-title{position:absolute;top:62px;width:100%;color:var(--orange)}
.about .divider{position:absolute;top:108px;left:530px;color:var(--orange)}
.about p{position:absolute;top:144px;left:336px;width:528px;font-size:9px;line-height:12px;color:var(--muted);text-align:center}
.stats{position:absolute;top:258px;left:328px;display:flex;gap:55px}
.stat{width:96px;text-align:center}
.stat .disc{width:90px;height:90px;border-radius:50%;background:var(--orange);margin:0 auto;display:flex;align-items:center;justify-content:center}
.stat .num{font-size:26px;color:var(--orange);margin-top:14px;font-weight:400}
.stat .lbl{font-size:9px;color:var(--muted);line-height:11px}

/* services */
.services{top:964px;height:498px;background:linear-gradient(180deg,#c6600d 0%,#d9761a 50%,#c8650f 100%);color:var(--white)}
.services .sec-title{position:absolute;top:40px;width:100%}
.services .divider{position:absolute;top:84px;left:530px;color:var(--white)}
.services .intro{position:absolute;top:118px;left:360px;width:480px;font-size:11px;line-height:14px;text-align:center}
.svc{position:absolute;width:217px}
.svc .photo{height:150px}
.svc h3{font-size:17px;font-weight:700;margin-top:10px;letter-spacing:.3px}
.svc ul{list-style:none;margin-top:6px;font-size:11px;line-height:20px}
.svc li{display:flex;align-items:center;gap:8px}
.svc-card{background:var(--white);color:var(--ink);padding:8px}
.svc-card h3{color:var(--orange)}
.svc-card ul{color:var(--muted)}

/* blog */
.blog{top:1462px;height:523px;background:linear-gradient(90deg,#f4f4f4 0%,#ecebea 60%,#e8e2dc 100%)}
.blog .sec-title{position:absolute;top:30px;width:100%;color:var(--orange)}
.blog .divider{position:absolute;top:74px;left:530px;color:var(--orange)}
.blog .intro{position:absolute;top:106px;left:250px;width:700px;font-size:9px;line-height:13px;color:var(--muted);text-align:center}
.post{position:absolute;top:199px;width:203px}
.post .photo{height:150px;border:4px solid var(--white);box-shadow:0 2px 5px rgba(0,0,0,.2)}
.post .meta{display:flex;justify-content:space-between;margin-top:36px;font-size:11px;color:var(--orange)}
.post p{margin-top:8px;font-size:9px;line-height:12px;color:var(--muted)}
.post .more{display:block;text-align:right;font-size:9px;color:var(--orange);margin-top:10px}

/* estimates */
.estimates{top:1985px;height:502px;background:linear-gradient(180deg,#c45f08 0%,#d8721a 100%);color:var(--white)}
.estimates .sec-title{position:absolute;top:36px;width:100%}
.estimates .divider{position:absolute;top:80px;left:530px;color:var(--white)}
.estimates .text{position:absolute;top:126px;left:240px;width:720px;font-size:11px;line-height:15.5px;text-align:center}
.estimates .text p{margin-bottom:30px}
.estimates .learn{position:absolute;top:442px;width:100%;text-align:center;font-size:16px;font-weight:700}

/* map */
.map{top:2487px;height:278px;background:linear-gradient(90deg,#eceae4 0%,#e6e3da 55%,#e9d49a 75%,#ecebe6 100%)}

/* footer */
.footer{top:2765px;height:245px;background:linear-gradient(180deg,#c9640e 0%,#d6711b 100%);color:var(--white)}
.fcol{position:absolute;top:48px}
.fcol h4{font-size:19px;font-weight:700;margin-bottom:12px}
.fcol p,.fcol li{font-size:9px;line-height:12px}
.fcol ul{list-style:none}
.fcol ul li{line-height:24px;border-bottom:1px solid rgba(255,255,255,.35);width:100px}
.tweet{margin-bottom:10px}
.contact-line{line-height:23px!important}
.copy{top:3010px;height:36px;background:#4d4d4d;color:#ddd;font-size:9px;display:flex;align-items:center}
.copy span{position:absolute;left:250px}
</style>
</head>
<body>

<header class="topbar">
  <div class="contact"><span>Phone Number : 0800 555 214</span><span>Email : info@portalia720.example</span><span>Address : Calle Ficticia 12, 28001</span></div>
  <div class="links"><span>THE GROUP</span><span>CAREER</span><span>PRESS AREA</span></div>
</header>

<header class="nav">
  <div class="brand"><span class="brand-mark"></span><span class="brand-name">Portalia720º</span></div>
  <nav class="menu"><span class="active">HOME</span><span>ABOUT US</span><span>SERVICES</span><span>BLOGS</span><span>CONTACT US</span></nav>
  <div class="login">LOG IN</div>
</header>

<section class="hero">
  <div class="hero-photo" role="img" aria-label="Brick house in a snowy winter landscape"></div>
  <div class="hero-band"></div>
  <h1>WELCOME TO PORTALIA720º</h1>
  <p>Lorem Ipsum is simply dummy text of the printing and typesetting industry. Lorem Ipsum has been the industry's standard dummy text ever since the 1500s.</p>
  <div class="btn-ghost">Read More</div>
  <div class="search">
    <div class="search-input">Ville, departement ou code postal</div>
    <div class="search-btn"><svg width="18" height="18" viewBox="0 0 20 20"><circle cx="8" cy="8" r="6" fill="none" stroke="#fff" stroke-width="2.5"/><line x1="12.5" y1="12.5" x2="18" y2="18" stroke="#fff" stroke-width="2.5"/></svg></div>
  </div>
</section>

<section class="about">
  <h2 class="sec-title">ABOUT US PORTALIA720º</h2>
  <div class="divider"></div>
  <p>Lorem Ipsum is simply dummy text of the printing and typesetting industry. Lorem Ipsum has been the industry's standard dummy text ever since the 1500s, when an unknown printer took a galley of type and scrambled it to make a type specimen book. It has survived not only five centuries, but also the leap into electronic typesetting, remaining essentially unchanged. It was popularised in the 1960s with the release of Letraset sheets containing Lorem Ipsum passages, and more recently with desktop publishing software like Aldus PageMaker including versions of Lorem Ipsum.</p>
  <div class="stats">
    <div class="stat"><div class="disc"><svg width="44" height="30" viewBox="0 0 44 30"><path d="M2 14 L12 6 L22 10 L32 6 L42 14 L30 26 L24 24 L14 26 Z" fill="#fff"/></svg></div><div class="num">1st</div><div class="lbl">Trustee of condominiums<br>France</div></div>
    <div class="stat"><div class="disc"><svg width="44" height="34" viewBox="0 0 44 34"><circle cx="22" cy="9" r="6" fill="#fff"/><circle cx="9" cy="13" r="4.5" fill="#fff"/><circle cx="35" cy="13" r="4.5" fill="#fff"/><path d="M12 32 Q22 14 32 32Z M1 30 Q9 18 16 28Z M28 28 Q35 18 43 30Z" fill="#fff"/></svg></div><div class="num">500</div><div class="lbl">agencies at your service</div></div>
    <div class="stat"><div class="disc"><svg width="40" height="40" viewBox="0 0 40 40"><circle cx="20" cy="16" r="12" fill="none" stroke="#fff" stroke-width="3"/><circle cx="20" cy="16" r="5" fill="#fff"/><path d="M13 26 L10 38 L20 33 L30 38 L27 26" fill="#fff"/></svg></div><div class="num">1st</div><div class="lbl">rental agency France</div></div>
    <div class="stat"><div class="disc"><svg width="40" height="36" viewBox="0 0 40 36"><path d="M20 2 L38 18 L33 18 L33 34 L24 34 L24 24 L16 24 L16 34 L7 34 L7 18 L2 18 Z" fill="#fff"/></svg></div><div class="num">45,000</div><div class="lbl">Property available</div></div>
  </div>
</section>

<section class="services">
  <h2 class="sec-title">SERVICES</h2>
  <div class="divider"></div>
  <p class="intro">Lorem Ipsum is simply dummy text of the printing and typesetting industry. Lorem Ipsum has been the industry's standard dummy text ever since the 1500s, when an unknown printer took a galley of type and scrambled it to make a type specimen book</p>

  <div class="svc" style="left:248px;top:177px">
    <div class="photo" role="img" aria-label="Office team working at a laptop" style="background:linear-gradient(135deg,#e9ecef,#b9c3cc 60%,#7b8a96)"></div>
    <h3>ADMINISTRATION</h3>
    <ul><li><svg width="10" height="8" viewBox="0 0 10 8"><path d="M1 4 L4 7 L9 1" fill="none" stroke="#fff" stroke-width="1.8"/></svg>Treasury</li><li><svg width="10" height="8" viewBox="0 0 10 8"><path d="M1 4 L4 7 L9 1" fill="none" stroke="#fff" stroke-width="1.8"/></svg>Accounting</li><li><svg width="10" height="8" viewBox="0 0 10 8"><path d="M1 4 L4 7 L9 1" fill="none" stroke="#fff" stroke-width="1.8"/></svg>Savings</li></ul>
  </div>

  <div class="svc svc-card" style="left:477px;top:169px;width:246px;height:278px">
    <div class="photo" role="img" aria-label="Business meeting around a conference table" style="background:linear-gradient(135deg,#dfe5ea,#aab5c0 60%,#6f7c88)"></div>
    <h3>CONSULTING</h3>
    <ul><li><svg width="10" height="8" viewBox="0 0 10 8"><path d="M1 4 L4 7 L9 1" fill="none" stroke="#777" stroke-width="1.8"/></svg>Legal</li><li><svg width="10" height="8" viewBox="0 0 10 8"><path d="M1 4 L4 7 L9 1" fill="none" stroke="#777" stroke-width="1.8"/></svg>Technical</li><li><svg width="10" height="8" viewBox="0 0 10 8"><path d="M1 4 L4 7 L9 1" fill="none" stroke="#777" stroke-width="1.8"/></svg>Regulatory</li></ul>
  </div>

  <div class="svc" style="left:735px;top:177px">
    <div class="photo" role="img" aria-label="Group of colleagues in a bright office" style="background:linear-gradient(135deg,#eef0f2,#b4bec8 55%,#4f5a66)"></div>
    <h3>MEDIATION</h3>
    <ul><li><svg width="10" height="8" viewBox="0 0 10 8"><path d="M1 4 L4 7 L9 1" fill="none" stroke="#fff" stroke-width="1.8"/></svg>Repairs</li><li><svg width="10" height="8" viewBox="0 0 10 8"><path d="M1 4 L4 7 L9 1" fill="none" stroke="#fff" stroke-width="1.8"/></svg>Meetings</li><li><svg width="10" height="8" viewBox="0 0 10 8"><path d="M1 4 L4 7 L9 1" fill="none" stroke="#fff" stroke-width="1.8"/></svg>Delinquency</li></ul>
  </div>
</section>

<section class="blog">
  <h2 class="sec-title">OUR BLOG</h2>
  <div class="divider"></div>
  <p class="intro">Lorem Ipsum is simply dummy text of the printing and typesetting industry. Lorem Ipsum has been the industry's standard dummy text ever since the 1500s, when an unknown printer took a galley of type and scrambled it to make a type specimen book. It has survived not only five centuries, but also the leap into electronic typesetting, remaining essentially unchanged. It was popularised in the 1960s with the release of Letraset sheets containing Lorem Ipsum passages, and more recently with desktop publishing software like Aldus PageMaker including versions of Lorem Ipsum.</p>

  <article class="post" style="left:250px">
    <div class="photo" role="img" aria-label="Colleagues gathered around a laptop" style="background:linear-gradient(135deg,#cfd6dc,#8c7f72 60%,#56616b)"></div>
    <div class="meta"><span>CONOCE NUESTREN</span><span>12:59 PM</span></div>
    <p>Lorem Ipsum is simply dummy text of typesetting, remaining essentially unchanged. Popularised in the 1960s with the release of Letraset sheets containing Lorem Ipsum passage and more desktop publishing software.</p>
    <span class="more">Read More</span>
  </article>
  <article class="post" style="left:493px">
    <div class="photo" role="img" aria-label="Overhead view of a team meeting at a round table" style="background:linear-gradient(135deg,#d9dcdf,#9aa2a9 60%,#6c747b)"></div>
    <div class="meta"><span>VELBRA NEREND</span><span>10:15 AM</span></div>
    <p>Lorem Ipsum is simply dummy text of typesetting, remaining essentially unchanged. Popularised in the 1960s with the release of Letraset sheets containing Lorem Ipsum passage and more desktop publishing software.</p>
    <span class="more">Read More</span>
  </article>
  <article class="post" style="left:741px">
    <div class="photo" role="img" aria-label="Business people at a desk in a modern office" style="background:linear-gradient(135deg,#eef0f1,#b6bcc1 55%,#3f4650)"></div>
    <div class="meta"><span>LAS COMUNIDADEN</span><span>03:45 PM</span></div>
    <p>Lorem Ipsum is simply dummy text of typesetting, remaining essentially unchanged. Popularised in the 1960s with the release of Letraset sheets containing Lorem Ipsum passage and more desktop publishing software.</p>
    <span class="more">Read More</span>
  </article>
</section>

<section class="estimates">
  <h2 class="sec-title">ESTIMATES</h2>
  <div class="divider"></div>
  <div class="text">
    <p>Lorem Ipsum is simply dummy text of the printing and typesetting industry. Lorem Ipsum has been the industry's standard dummy text ever since the 1500s, when an unknown printer took a galley of type and scrambled it to make a type specimen book. It has survived not only five centuries, but also the leap into electronic typesetting, remaining essentially unchanged. It was popularised in the 1960s with the release of Letraset sheets containing Lorem Ipsum passages, and more recently with desktop publishing software like Aldus PageMaker. Lorem Ipsum is simply dummy text of the printing and typesetting industry. Lorem Ipsum has been the industry's standard release of Letraset sheets including versions of Lorem Ipsum.</p>
    <p>Lorem Ipsum is simply dummy text of the printing and typesetting industry. Lorem Ipsum has been the industry's standard dummy text ever since the 1500s, when an unknown printer took a galley of type and scrambled it to make a type specimen book. It has survived not only five centuries, including versions of Lorem Ipsum and software like Aldus PageMaker including versions of Lorem Ipsum.</p>
    <p>Lorem Ipsum is simply dummy text of the printing and typesetting industry. Lorem Ipsum survived not only five centuries, but also the leap into electronic typesetting, remaining essentially unchanged including versions of Lorem Ipsum.</p>
  </div>
  <div class="learn">LEARN MORE</div>
</section>

<section class="map" role="img" aria-label="Street map of the office area and surroundings"></section>

<footer class="footer">
  <div class="fcol" style="left:256px;width:170px">
    <h4>ABOUT US</h4>
    <p>Lorem Ipsum is simply dummy text of the printing and typesetting industry. Lorem Ipsum has been the industry's standard dummy text ever since the 1500s, when an unknown printer took a galley of type and scrambled it to make a type specimen book. It has survived essentially unchanged.</p>
  </div>
  <div class="fcol" style="left:459px">
    <h4>HOME LINK</h4>
    <ul><li>HOME</li><li>ABOUT US</li><li>SERVICES</li><li>BLOGS</li><li>CONTACT US</li></ul>
  </div>
  <div class="fcol" style="left:601px;width:160px">
    <h4>RECENT TWEETS</h4>
    <p class="tweet">Lorem ipsum dolor sit amet, consectetur adipiscing elit, sed do eiusmod<br>2 hours ago</p>
    <p class="tweet">Lorem ipsum dolor sit amet, consectetur adipiscing elit, sed do eiusmod<br>3 hours ago</p>
    <p class="tweet">Lorem ipsum dolor sit amet, consectetur adipiscing elit, sed do eiusmod<br>4 hours ago</p>
  </div>
  <div class="fcol" style="left:790px;width:170px">
    <h4>CONTACT US</h4>
    <p>Lorem ipsum dolor sit amet, consectetur adipiscing elit, sed do eiusmod tempor incididunt ut labore et dolore magna.</p>
    <p class="contact-line">Ph.: + 0800 555 301</p>
    <p class="contact-line">Fax.: + 0800 555 302</p>
    <p class="contact-line">Email: info@portalia720.example</p>
  </div>
</footer>

<footer class="copy"><span>Copyright © 2016 Portalia720º. All Right Reserved.</span></footer>

</body>
</html>
```